UVANTA Virtualizing the computer, making it live in the cloud

We plan to visualize the computer, essentially making all your computing, storage, security, processing, etc done in the cloud. We feel this will revolutionize the entire computer industry.
We have a logo design which has been included here. We want this sharp, progressive and also frameworked in a way that we can sell our monthly service as well as computers online through this site.

Target Market(s)

Laptop users, Millennials, college educated people.

Industry/Entity Type

Computer

Number of Pages Required

5+ page

Font styles to use
Serif
Sans Serif

Colors

Designer to choose colors to be used in the design.

Requirements
Must have
• eCommerce capable. Frameworked for people to enroll in our program and pay for the service online. Would prefer to allow people from multiple countries to enroll and use our service

```html
<!DOCTYPE html>
<html lang="en">
<head>
<meta charset="utf-8">
<title>UVANTA — Cloud Storage &amp; Hosting</title>
<link rel="stylesheet" href="https://fonts.googleapis.com/css2?family=Montserrat:wght@400;500;600;700&family=Open+Sans:wght@400;600;700&display=swap">
<style>
:root{
  --blue:#2f8fe6;
  --blue-light:#7db9f2;
  --navy:#273344;
  --ink:#1f2a37;
  --text:#3b4450;
  --muted:#8a939e;
  --line:#e6e9ee;
  --row:#f6f7f9;
  --pale:#eef3f8;
  --badge:#4a5562;
  --white:#ffffff;
  --green:#25b865;
  --red:#e8453c;
  --red-dark:#c9362e;
  --olive:#9bb93a;
  --amber:#f3b93a;
}
*{box-sizing:border-box;margin:0;padding:0}
html,body{width:1200px;height:3147px;overflow:hidden}
body{font-family:"Open Sans",Arial,sans-serif;color:var(--text);background:var(--white);position:relative}
.abs{position:absolute}
.head{font-family:"Montserrat",Arial,sans-serif}
a{color:inherit;text-decoration:none}

/* top bar */
.topbar{position:absolute;top:0;left:0;width:1200px;height:38px;border-bottom:1px solid var(--line);font-size:9px;color:var(--ink)}
.topbar .lang{left:160px;top:13px}
.topbar .contact{top:13px;display:flex;align-items:center;gap:5px;white-space:nowrap}
.client-area{position:absolute;left:923px;top:0;width:114px;height:38px;background:var(--blue);color:var(--white);font-size:9.5px;font-weight:600;display:flex;align-items:center;justify-content:center;gap:8px}

/* nav */
.nav{position:absolute;top:38px;left:0;width:1200px;height:77px}
.brand{position:absolute;left:164px;top:24px;font-family:"Montserrat",Arial,sans-serif;font-weight:700;font-size:21px;color:var(--blue);display:flex;align-items:center;gap:6px;letter-spacing:.5px}
.brand .dot{width:10px;height:10px;border-radius:50%;background:#f4b728}
.menu{position:absolute;left:319px;top:36px;font-family:"Montserrat",Arial,sans-serif;font-size:8.5px;font-weight:600;color:var(--blue)}
.menu a{position:absolute;white-space:nowrap}
.menu a.active{color:var(--ink)}
.cart{position:absolute;left:1003px;top:32px;display:flex;align-items:center;gap:6px}
.cart .count{background:var(--blue);color:var(--white);font-size:8.5px;width:15px;height:15px;display:flex;align-items:center;justify-content:center;border-radius:2px}

/* hero */
.hero{position:absolute;top:115px;left:0;width:1200px;height:430px;background:var(--blue);color:var(--white);overflow:hidden}
.hero .kicker{left:160px;top:104px;font-size:10.5px;font-weight:600}
.hero h1{position:absolute;left:160px;top:130px;font-family:"Montserrat",Arial,sans-serif;font-size:23px;line-height:34px;font-weight:700}
.hero .sub{left:160px;top:211px;font-size:11.5px}
.btn{display:inline-flex;align-items:center;justify-content:center;gap:8px;font-family:"Montserrat",Arial,sans-serif;font-size:9.5px;font-weight:700;text-transform:uppercase;color:var(--white);border-radius:2px;white-space:nowrap}
.btn-dark{background:var(--navy)}
.btn-blue{background:var(--blue)}
.hero .cta{position:absolute;left:160px;top:290px;width:159px;height:38px}
.hero .pricing-link{left:333px;top:304px;font-size:9.5px;font-weight:700;font-family:"Montserrat",Arial,sans-serif;text-transform:uppercase}
.hero-art{position:absolute;left:500px;top:10px;width:560px;height:360px;background:radial-gradient(ellipse at 55% 50%,rgba(255,255,255,.38) 0%,rgba(255,255,255,.18) 40%,rgba(255,255,255,0) 70%)}

/* domain search */
.domain{position:absolute;top:545px;left:0;width:1200px;height:154px;background:var(--navy);color:var(--white)}
.domain .label{left:160px;top:52px;font-family:"Montserrat",Arial,sans-serif;font-size:12px;font-weight:600;line-height:20px}
.domain .field{position:absolute;left:340px;top:47px;width:503px;height:40px;background:var(--white);border-radius:2px;font-size:9.5px;color:#9aa3ad;padding:14px 20px}
.domain .search{position:absolute;left:852px;top:47px;width:142px;height:40px}
.domain .tlds{position:absolute;left:340px;top:100px;font-size:10px}
.tld{position:absolute;display:flex;align-items:center;gap:6px;white-space:nowrap}
.box{width:14px;height:14px;background:var(--white);border-radius:2px;display:flex;align-items:center;justify-content:center}
.box.checked{background:var(--blue)}

/* why */
.why{position:absolute;top:699px;left:0;width:1200px;height:392px;border-bottom:1px solid var(--line)}
.section-title{position:absolute;left:0;width:1200px;text-align:center;font-family:"Montserrat",Arial,sans-serif;font-size:20px;font-weight:500;color:var(--ink);line-height:31px}
.section-title em{font-style:normal;color:var(--blue)}
.feature{position:absolute;top:164px;width:300px;text-align:center}
.feature .icon{display:block;width:66px;height:66px;margin:0 auto}
.feature h3{font-family:"Montserrat",Arial,sans-serif;font-size:13.5px;font-weight:500;color:var(--ink);margin-top:24px}
.feature p{font-size:10px;line-height:21px;color:var(--muted);margin-top:12px}

/* pricing */
.pricing{position:absolute;top:1091px;left:0;width:1200px;height:590px}
.plans{position:absolute;left:162px;top:147px;width:878px;height:399px;border:1px solid var(--line)}
.plan{position:absolute;top:0;width:219.5px;height:397px;text-align:center}
.plan.featured{top:-6px;height:409px;padding-top:6px;box-shadow:0 0 0 2px var(--blue);background:var(--white);z-index:2}
.plan h4{font-family:"Montserrat",Arial,sans-serif;font-size:9.5px;font-weight:700;color:var(--ink);margin-top:30px}
.plan .picon{display:block;margin:10px auto 0;width:40px;height:36px}
.plan .price{font-family:"Montserrat",Arial,sans-serif;font-size:21px;font-weight:700;color:var(--ink);margin-top:8px}
.plan .price small{font-weight:400;font-size:16px}
.plan .for{font-size:8px;color:var(--muted);margin-top:3px}
.plan ul{list-style:none;margin-top:24px;text-align:left}
.plan li{height:31.5px;display:flex;align-items:center;gap:12px;padding-left:18px;font-size:8.5px;color:var(--text)}
.plan li:nth-child(odd){background:var(--row)}
.plan .btn{width:126px;height:34px;margin-top:27px}

/* promo rows */
.art{position:absolute}
.promo h2{position:absolute;font-family:"Montserrat",Arial,sans-serif;font-size:18.5px;font-weight:500;color:var(--ink);line-height:31px}
.promo p{position:absolute;font-size:10.5px;line-height:23px;color:var(--muted)}

/* clients */
.clients{position:absolute;top:2419px;left:0;width:1200px;height:277px;background:var(--pale)}
.client-mark{position:absolute;top:160px;width:64px;height:36px;background:var(--badge);border-radius:3px}
.client-mark.round{border-radius:50%;width:48px;height:48px;top:154px}

/* cta band */
.cta-band{position:absolute;top:2696px;left:0;width:1200px;height:116px;background:var(--blue);color:var(--white)}
.cta-band .msg{left:243px;top:45px;font-family:"Montserrat",Arial,sans-serif;font-size:18px;font-weight:500}
.cta-band .btn{position:absolute;left:852px;top:40px;width:128px;height:35px}

/* footer */
.footer{position:absolute;top:2812px;left:0;width:1200px;height:335px;font-size:9.5px;color:var(--text)}
.footer h5{position:absolute;top:80px;font-family:"Montserrat",Arial,sans-serif;font-size:12px;font-weight:600;color:var(--ink)}
.footer .links{position:absolute;top:113px;line-height:22.5px;font-size:9.5px;color:var(--text)}
.footer .brand{left:160px;top:72px}
.footer .about{left:160px;top:117px;width:200px;line-height:18px;color:var(--ink)}
.socials{position:absolute;left:164px;top:210px;display:flex;gap:8px}
.socials span{width:20px;height:20px;border-radius:50%;border:1px solid #c9ced5}
.socials span.on{border-color:var(--blue)}
.copy{left:160px;top:270px;font-size:9px;line-height:19px;color:var(--muted)}
.footer .ci{position:absolute;left:835px;display:flex;align-items:center;gap:10px;font-size:9px;color:var(--muted)}
.footer .send{position:absolute;left:835px;top:173px;width:126px;height:34px}
.chat{position:absolute;left:965px;top:3107px;width:218px;height:40px;background:var(--blue);color:var(--white);border-radius:8px 8px 0 0;font-family:"Montserrat",Arial,sans-serif;font-size:10.5px;font-weight:600;display:flex;align-items:center;justify-content:center;gap:8px}
.chat i{width:6px;height:6px;border-radius:50%;background:var(--white);display:inline-block}
</style>
</head>
<body>

<header class="topbar">
  <span class="abs lang">en &#9662;</span>
  <span class="contact abs" style="left:700px">
    <svg width="10" height="10" viewBox="0 0 24 24"><path fill="#1f2a37" d="M6.6 10.8a15 15 0 0 0 6.6 6.6l2.2-2.2c.3-.3.7-.4 1-.2 1.1.4 2.3.6 3.6.6.6 0 1 .4 1 1V20c0 .6-.4 1-1 1A17 17 0 0 1 3 4c0-.6.4-1 1-1h3.5c.6 0 1 .4 1 1 0 1.3.2 2.5.6 3.6.1.3 0 .7-.2 1z"/></svg>
    +1 555 0142 889
  </span>
  <span class="contact abs" style="left:800px">
    <svg width="11" height="9" viewBox="0 0 22 16"><rect x="1" y="1" width="20" height="14" fill="none" stroke="#1f2a37" stroke-width="2"/><path d="M1 1l10 8 10-8" fill="none" stroke="#1f2a37" stroke-width="2"/></svg>
    support@uvanta.com
  </span>
  <a class="client-area" href="#">
    <svg width="10" height="10" viewBox="0 0 24 24"><circle cx="12" cy="7" r="5" fill="#fff"/><path d="M2 23c0-6 4.5-9 10-9s10 3 10 9z" fill="#fff"/></svg>
    Client area
  </a>
</header>

<nav class="nav">
  <div class="brand"><span class="dot"></span>UVANTA</div>
  <div class="menu">
    <a class="active" style="left:0">HOME</a>
    <a style="left:69px">PRODUCTS</a>
    <a style="left:159px">STORAGE</a>
    <a style="left:245px">PROCESSING</a>
    <a style="left:342px">HOSTING</a>
    <a style="left:426px">FACTS</a>
    <a style="left:493px">SITE PROTECTION</a>
    <a style="left:610px">CONTACT</a>
  </div>
  <div class="cart">
    <svg width="14" height="12" viewBox="0 0 24 20"><path d="M1 1h4l3 12h12l3-9H7" fill="none" stroke="#1f2a37" stroke-width="2"/><circle cx="9" cy="17" r="2" fill="#1f2a37"/><circle cx="19" cy="17" r="2" fill="#1f2a37"/></svg>
    <span class="count">2</span>
  </div>
</nav>

<section class="hero">
  <p class="abs kicker">Welcome To UVANTA</p>
  <h1>Visualize Your Computer<br>with Cloud Storage.</h1>
  <p class="abs sub">Powerfull Cloud Hosting Built for Everyone</p>
  <a class="btn btn-dark cta" href="#">
    <svg width="10" height="10" viewBox="0 0 24 24"><path d="M3 21l4-1L20 7l-3-3L4 17z" fill="#fff"/></svg>
    Get started now
  </a>
  <a class="abs pricing-link" href="#">Check pricing</a>
  <div class="hero-art" role="img" aria-label="Illustration of a desktop monitor connected to cloud storage, with a light bulb, clouds, cursor and gears"></div>
</section>

<section class="domain">
  <p class="abs label">Search your domain,<br>purchase one.</p>
  <div class="field">Enter your domain name here</div>
  <a class="btn btn-blue search" href="#">Search domain</a>
  <div class="tlds">
    <span class="tld" style="left:0"><span class="box checked"><svg width="9" height="9" viewBox="0 0 12 12"><path d="M2 6l3 3 5-6" fill="none" stroke="#fff" stroke-width="2"/></svg></span>.com</span>
    <span class="tld" style="left:59px"><span class="box"></span>.net</span>
    <span class="tld" style="left:113px"><span class="box"></span>.org</span>
    <span class="tld" style="left:185px"><span class="box"></span>.in</span>
  </div>
</section>

<section class="why">
  <h2 class="section-title" style="top:62px">Lots of Cloud Storage services in town.<br>Why you should <em>choose us?</em></h2>
  <div class="feature" style="left:144px">
    <svg class="icon" viewBox="0 0 66 66" role="img" aria-label="Padlock icon">
      <path d="M21 30V20a12 12 0 0 1 24 0v10" fill="none" stroke="var(--green)" stroke-width="5"/>
      <rect x="13" y="29" width="40" height="32" rx="4" fill="var(--red)"/>
      <rect x="13" y="29" width="20" height="32" rx="4" fill="var(--red-dark)" opacity=".35"/>
      <circle cx="33" cy="42" r="4" fill="#fff"/>
      <rect x="31.5" y="44" width="3" height="8" fill="#fff"/>
    </svg>
    <h3>Secure &amp; Powerfull</h3>
    <p>Easily configurable with your popular CMS<br>platforms - PagePress, SiteJam &amp; more.</p>
  </div>
  <div class="feature" style="left:437px">
    <svg class="icon" viewBox="0 0 66 66" role="img" aria-label="Server rack icon">
      <rect x="12" y="6" width="42" height="14" rx="2" fill="var(--olive)"/>
      <rect x="12" y="24" width="42" height="14" rx="2" fill="var(--olive)"/>
      <rect x="12" y="42" width="42" height="14" rx="2" fill="var(--amber)"/>
      <circle cx="19" cy="13" r="2.5" fill="#fff"/><circle cx="19" cy="31" r="2.5" fill="#fff"/><circle cx="19" cy="49" r="2.5" fill="#fff"/>
      <path d="M28 13h20M28 31h20M28 49h20" stroke="#fff" stroke-width="2"/>
      <path d="M33 56v6M20 62h26" stroke="var(--ink)" stroke-width="2"/>
    </svg>
    <h3>Computer Storage</h3>
    <p>Easily configurable with your popular CMS<br>platforms - PagePress, SiteJam &amp; more.</p>
  </div>
  <div class="feature" style="left:752px">
    <svg class="icon" viewBox="0 0 66 66" role="img" aria-label="Umbrella icon">
      <path d="M7 32a26 24 0 0 1 52 0c-4-3-9-3-13 0-4-3-9-3-13 0-4-3-9-3-13 0-4-3-9-3-13 0z" fill="var(--blue)"/>
      <path d="M33 8a10 24 0 0 0-7 24M33 8a10 24 0 0 1 7 24" fill="none" stroke="#1f7fd8" stroke-width="1.5"/>
      <path d="M33 32v22a5 5 0 0 1-10 0" fill="none" stroke="var(--red)" stroke-width="3" stroke-linecap="round"/>
    </svg>
    <h3>Privacy Protected</h3>
    <p>Easily configurable with your popular CMS<br>platforms - PagePress, SiteJam &amp; more.</p>
  </div>
</section>

<section class="pricing">
  <h2 class="section-title" style="top:66px">Pay for what you <em>actually</em> use. No hidden charge!</h2>
  <div class="plans">
    <div class="plan" style="left:0">
      <h4>PERSONAL</h4>
      <svg class="picon" viewBox="0 0 40 36"><circle cx="20" cy="10" r="7" fill="none" stroke="#2f8fe6" stroke-width="2"/><path d="M7 34c0-9 6-13 13-13s13 4 13 13z" fill="none" stroke="#1f2a37" stroke-width="2"/></svg>
      <p class="price">$3<small>/mo</small></p>
      <p class="for">best for personal use</p>
      <ul>
        <li><svg width="10" height="10" viewBox="0 0 12 12"><path d="M1 6l3.5 3.5L11 2" fill="none" stroke="#25b865" stroke-width="2"/></svg>10GB Space</li>
        <li><svg width="10" height="10" viewBox="0 0 12 12"><path d="M1 6l3.5 3.5L11 2" fill="none" stroke="#25b865" stroke-width="2"/></svg>1 Free Domain</li>
        <li><svg width="10" height="10" viewBox="0 0 12 12"><path d="M1 6l3.5 3.5L11 2" fill="none" stroke="#25b865" stroke-width="2"/></svg>300GB SSD Disk</li>
        <li><svg width="10" height="10" viewBox="0 0 12 12"><path d="M2 2l8 8M10 2l-8 8" stroke="#e8453c" stroke-width="2"/></svg>Special Offers</li>
        <li><svg width="10" height="10" viewBox="0 0 12 12"><path d="M1 6l3.5 3.5L11 2" fill="none" stroke="#25b865" stroke-width="2"/></svg>Unlimited Support</li>
      </ul>
      <a class="btn btn-blue" href="#">Get started now</a>
    </div>
    <div class="plan featured" style="left:219.5px">
      <h4>SMALL TEAM</h4>
      <svg class="picon" viewBox="0 0 40 36"><circle cx="20" cy="9" r="6" fill="none" stroke="#2f8fe6" stroke-width="2"/><circle cx="8" cy="13" r="4" fill="none" stroke="#1f2a37" stroke-width="2"/><circle cx="32" cy="13" r="4" fill="none" stroke="#1f2a37" stroke-width="2"/><path d="M9 34c0-8 5-12 11-12s11 4 11 12zM1 32c0-6 3-9 7-9M39 32c0-6-3-9-7-9" fill="none" stroke="#1f2a37" stroke-width="2"/></svg>
      <p class="price">$7<small>/mo</small></p>
      <p class="for">best for small team or startup</p>
      <ul>
        <li><svg width="10" height="10" viewBox="0 0 12 12"><path d="M1 6l3.5 3.5L11 2" fill="none" stroke="#25b865" stroke-width="2"/></svg>10GB Space</li>
        <li><svg width="10" height="10" viewBox="0 0 12 12"><path d="M1 6l3.5 3.5L11 2" fill="none" stroke="#25b865" stroke-width="2"/></svg>1 Free Domain</li>
        <li><svg width="10" height="10" viewBox="0 0 12 12"><path d="M1 6l3.5 3.5L11 2" fill="none" stroke="#25b865" stroke-width="2"/></svg>300GB SSD Disk</li>
        <li><svg width="10" height="10" viewBox="0 0 12 12"><path d="M2 2l8 8M10 2l-8 8" stroke="#e8453c" stroke-width="2"/></svg>Special Offers</li>
        <li><svg width="10" height="10" viewBox="0 0 12 12"><path d="M1 6l3.5 3.5L11 2" fill="none" stroke="#25b865" stroke-width="2"/></svg>Unlimited Support</li>
      </ul>
      <a class="btn btn-blue" href="#">Get started now</a>
    </div>
    <div class="plan" style="left:439px">
      <h4>COMPANY</h4>
      <svg class="picon" viewBox="0 0 40 36"><path d="M4 17L20 3l16 14" fill="none" stroke="#1f2a37" stroke-width="2"/><path d="M9 14v20h22V14" fill="none" stroke="#1f2a37" stroke-width="2"/><rect x="16" y="22" width="8" height="12" fill="none" stroke="#2f8fe6" stroke-width="2"/></svg>
      <p class="price">$15<small>/mo</small></p>
      <p class="for">best for company or agency</p>
      <ul>
        <li><svg width="10" height="10" viewBox="0 0 12 12"><path d="M1 6l3.5 3.5L11 2" fill="none" stroke="#25b865" stroke-width="2"/></svg>10GB Space</li>
        <li><svg width="10" height="10" viewBox="0 0 12 12"><path d="M1 6l3.5 3.5L11 2" fill="none" stroke="#25b865" stroke-width="2"/></svg>1 Free Domain</li>
        <li><svg width="10" height="10" viewBox="0 0 12 12"><path d="M1 6l3.5 3.5L11 2" fill="none" stroke="#25b865" stroke-width="2"/></svg>300GB SSD Disk</li>
        <li><svg width="10" height="10" viewBox="0 0 12 12"><path d="M2 2l8 8M10 2l-8 8" stroke="#e8453c" stroke-width="2"/></svg>Special Offers</li>
        <li><svg width="10" height="10" viewBox="0 0 12 12"><path d="M1 6l3.5 3.5L11 2" fill="none" stroke="#25b865" stroke-width="2"/></svg>Unlimited Support</li>
      </ul>
      <a class="btn btn-blue" href="#">Get started now</a>
    </div>
    <div class="plan" style="left:657px">
      <h4>BIG SHOT</h4>
      <svg class="picon" viewBox="0 0 40 36"><circle cx="20" cy="18" r="15" fill="none" stroke="#2f8fe6" stroke-width="2"/><path d="M5 18h30M20 3c-6 5-6 25 0 30M20 3c6 5 6 25 0 30" fill="none" stroke="#1f2a37" stroke-width="1.6"/></svg>
      <p class="price">$25<small>/mo</small></p>
      <p class="for">who wants everything unlimited!</p>
      <ul>
        <li><svg width="10" height="10" viewBox="0 0 12 12"><path d="M1 6l3.5 3.5L11 2" fill="none" stroke="#25b865" stroke-width="2"/></svg>10GB Space</li>
        <li><svg width="10" height="10" viewBox="0 0 12 12"><path d="M1 6l3.5 3.5L11 2" fill="none" stroke="#25b865" stroke-width="2"/></svg>1 Free Domain</li>
        <li><svg width="10" height="10" viewBox="0 0 12 12"><path d="M1 6l3.5 3.5L11 2" fill="none" stroke="#25b865" stroke-width="2"/></svg>300GB SSD Disk</li>
        <li><svg width="10" height="10" viewBox="0 0 12 12"><path d="M2 2l8 8M10 2l-8 8" stroke="#e8453c" stroke-width="2"/></svg>Special Offers</li>
        <li><svg width="10" height="10" viewBox="0 0 12 12"><path d="M1 6l3.5 3.5L11 2" fill="none" stroke="#25b865" stroke-width="2"/></svg>Unlimited Support</li>
      </ul>
      <a class="btn btn-blue" href="#">Get started now</a>
    </div>
  </div>
</section>

<section class="promo speed">
  <div class="art" style="left:150px;top:1690px;width:460px;height:290px;background:radial-gradient(ellipse at 50% 55%,#9cc9f3 0%,#cfe3f7 38%,rgba(255,255,255,0) 70%)" role="img" aria-label="Illustration of a server rack, cloud, gears and a monitor showing code"></div>
  <h2 style="left:661px;top:1758px">Super speed for your Cloud<br>Hosting to impress your visitor.</h2>
  <p style="left:661px;top:1831px">Get the best speed for your storage. Don't lose anymore<br>clients for the slowest speed of your hosting service.</p>
  <a class="btn btn-blue abs" style="left:663px;top:1901px;width:155px;height:36px" href="#">
    <svg width="10" height="10" viewBox="0 0 24 24"><path d="M3 21l4-1L20 7l-3-3L4 17z" fill="#fff"/></svg>
    Get started now
  </a>
</section>

<section class="promo dedicated">
  <h2 style="left:212px;top:2054px">Dedicated &amp; Secured server<br>for your Data.</h2>
  <p style="left:212px;top:2127px">Get the best speed for your website. Don't lose anymore<br>clients for the slowest speed of your hosting service.</p>
  <a class="btn btn-dark abs" style="left:212px;top:2255px;width:134px;height:36px" href="#">Read more</a>
  <a class="abs head" style="left:367px;top:2268px;font-size:9px;font-weight:600;color:var(--blue)" href="#">GET STARTED NOW</a>
  <div class="art" style="left:690px;top:2010px;width:360px;height:340px;background:radial-gradient(ellipse at 50% 50%,#5ea8ee 0%,#a9d0f5 40%,rgba(255,255,255,0) 70%)" role="img" aria-label="Illustration of a rocket launching from a desktop monitor among clouds and gears"></div>
</section>

<section class="clients">
  <h2 class="section-title" style="top:63px">We give <em>awesome service</em>,<br>Some of our trusted clients.</h2>
  <span class="client-mark" style="left:166px"></span>
  <span class="client-mark round" style="left:334px"></span>
  <span class="client-mark round" style="left:494px"></span>
  <span class="client-mark" style="left:640px;width:52px;height:44px;top:156px"></span>
  <span class="client-mark" style="left:806px;width:52px;height:44px;top:156px"></span>
  <span class="client-mark" style="left:943px;width:80px;height:30px;top:163px"></span>
</section>

<section class="cta-band">
  <p class="abs msg">20,000+ People trust UVANTA! Be one of them today.</p>
  <a class="btn btn-dark" href="#">Get started now</a>
</section>

<footer class="footer">
  <div class="brand"><span class="dot"></span>UVANTA</div>
  <p class="abs about">Lorem ipsum dolor sit amet, consectetuer adipiscing elit, sed diam nonummy nibh eui smod tincidunt ut laoreet dolore magna.</p>
  <div class="socials"><span></span><span class="on"></span><span></span><span></span><span></span></div>
  <p class="abs copy">© Copyright 2017 UVANTA<br>All Rights Reserved</p>

  <h5 style="left:384px">Important Links</h5>
  <div class="links" style="left:384px">Support<br>Privacy &amp; Policy<br>Terms &amp; Conditions<br>VPN Service<br>Dedicated Server</div>

  <h5 style="left:611px">SiteMap</h5>
  <div class="links" style="left:611px;top:105px">HOME<br>PRODUCTS<br>Storage<br>Processing<br>HOSTING<br>FACTS<br>SITE PROTECTION<br>CONTACT</div>

  <h5 style="left:835px">Contact with us</h5>
  <p class="ci" style="top:115px"><svg width="10" height="10" viewBox="0 0 24 24"><path fill="#8a939e" d="M6.6 10.8a15 15 0 0 0 6.6 6.6l2.2-2.2c.3-.3.7-.4 1-.2 1.1.4 2.3.6 3.6.6.6 0 1 .4 1 1V20c0 .6-.4 1-1 1A17 17 0 0 1 3 4c0-.6.4-1 1-1h3.5c.6 0 1 .4 1 1 0 1.3.2 2.5.6 3.6.1.3 0 .7-.2 1z"/></svg>+1 555 0142 889</p>
  <p class="ci" style="top:138px"><svg width="11" height="9" viewBox="0 0 22 16"><rect x="1" y="1" width="20" height="14" fill="none" stroke="#8a939e" stroke-width="2"/><path d="M1 1l10 8 10-8" fill="none" stroke="#8a939e" stroke-width="2"/></svg>support@uvanta.com</p>
  <a class="btn btn-blue send" href="#">Send us a message</a>
</footer>

<a class="chat" href="#">Chat with us <i></i> Online</a>

</body>
</html>
```